依頼詳細
★TOPラフ案について

・トップページの掲載内容はエクセルで作成した資料を添付しました。
仕様はワイヤーフレームのみですので、掲載情報が正しければ、お好きなデザインにて調整していただいて構いません。

掲載している情報のレイアウト通りではなくて大丈夫ですので
皆さまの感性にてお願いいたします。

・配置やデザイン等はアレンジしていただいて構いません。

・サイズは横幅2000pxで制作をお願いします。
縦に制限はありません。(コンテンツ幅は1100px~1200px内でお願いします。)
レスポンシブデザインのサイトで、bootstrap4を利用し、コーディングする予定になります。

・カラーイメージ
白を基調としてサブに青系、ワンポイントに赤色にてお願いします。

・ロゴ画像はヘッダーに入れる予定です。
(ロゴは青色(#00008B)で会社名ローマ字表示となります。頭文字は赤色(#FF3737)です。)

・デザインイメージ
誠実なデザインのイメージです。

デザイン選定後、決定した方には、正式な社名や連絡先を入れた修正をお願いしたいのと、
その他常識範囲で修正を依頼することもあります。
※以後、希望があれば中ページ作成及び他の案件コンテンツも継続してご依頼可能です。
ページ数
1ページ
希望イメージ
シンプル 複雑
単色 カラフル
暗い 明るい
日常 高級
遊び心 厳粛
未来的 伝統的
女性的 男性的
希望する色
青系
納品ファイル
• 高解像度JPG (.jpg)
• フォトショップ形式 (.psd)
補足説明
※ワイヤーフレーム通りのデザインでなくて、構いません。
メインビジュアル、素材などもお好みでデザインいただいて問題ございません。

仕様素材につきましてはKORVE定額素材内で使用可能な素材をご選択いただいてご使用ください。
(添付したデータ内にない素材でもご利用OKです。
その際は選定後素材№をお知らせください。)

依頼したイメージに沿ったデザインを作成いただけたためこちらのデザインに決めさせていただきました。

多くの提案をいただき本当にありがとうございました。
次回の依頼の際も是非提案いただけますようお願いいたします。

```html
<!DOCTYPE html>
<html lang="ja">
<head>
<meta charset="utf-8">
<title>物流梱包サービス トップページ</title>
<link href="https://fonts.googleapis.com/css2?family=Noto+Sans+JP:wght@400;500;700&family=Noto+Serif+JP:wght@400;500;600&family=Playfair+Display:wght@400;500&display=swap" rel="stylesheet">
<style>
:root{
  --navy:#00008b;
  --navy-deep:#0a1a5c;
  --blue:#1b3a8f;
  --blue-panel:#16306f;
  --red:#ff3737;
  --ink:#333;
  --muted:#888;
  --line:#e3e3e8;
  --bg:#ffffff;
  --tint:#eef1f8;
}
*{margin:0;padding:0;box-sizing:border-box}
html,body{width:1200px;height:2388px;overflow:hidden;background:var(--bg)}
body{position:relative;font-family:"Noto Sans JP",sans-serif;color:var(--ink)}
.abs{position:absolute}

/* header */
.site-header{left:0;top:0;width:1200px;height:150px}
.brand{left:40px;top:28px;font-family:"Noto Sans JP",sans-serif;font-weight:700;font-size:26px;letter-spacing:4px;color:var(--navy)}
.global-nav{left:420px;top:110px;display:flex;gap:44px;font-size:12px;color:var(--ink)}
.header-cta{right:0;top:0;display:flex}
.header-cta a{display:block;height:34px;line-height:34px;font-size:11px;color:#fff;text-decoration:none;padding:0 18px}
.header-cta .tel{background:var(--navy)}
.header-cta .mail{background:var(--red)}

/* hero */
.hero{left:0;top:150px;width:1200px;height:480px;background:linear-gradient(90deg,#6b8fb8 0%,#c9d4e2 35%,#f4f4f2 50%,#c9d4e2 65%,#5f7fa8 100%)}
.hero-copy{left:570px;top:190px;writing-mode:vertical-rl;font-family:"Noto Serif JP",serif;font-size:22px;letter-spacing:6px;color:var(--navy-deep);line-height:1.9}
.stripe{height:6px}

/* information */
.section-title{font-family:"Playfair Display",serif;font-weight:400;color:var(--ink);text-align:center}
.section-sub{font-size:11px;color:var(--red);text-align:center;margin-top:4px}
.info{left:0;top:660px;width:1200px;height:360px}
.info-bg{left:0;top:660px;width:1200px;height:360px;background:linear-gradient(160deg,#fff 40%,var(--tint) 100%)}
.info-head{left:0;top:680px;width:1200px}
.info-head .section-title{font-size:48px}
.news{left:260px;top:815px;width:680px;list-style:none}
.news li{display:flex;align-items:center;height:30px;border-bottom:1px solid var(--line);font-size:11px}
.news time{width:80px;color:var(--muted)}
.news .tag{background:var(--red);color:#fff;font-size:9px;padding:1px 10px;margin-right:24px}
.news .text{color:#999}

/* about */
.about-photo{left:0;top:1075px;width:660px;height:285px;background:linear-gradient(135deg,#e9ecef 0%,#b9c0c8 55%,#8a939c 100%)}
.panel{background:linear-gradient(135deg,var(--blue) 0%,var(--blue-panel) 60%,#0c1f55 100%);color:#fff}
.panel .heading{font-family:"Playfair Display",serif;font-size:52px;line-height:1}
.panel .sub{font-size:11px;color:#ff8a8a;margin-top:4px}
.panel p{font-size:11px;line-height:2;margin-top:22px}
.panel .more{display:inline-block;margin-top:20px;border:1px solid #fff;font-size:10px;padding:6px 36px;letter-spacing:2px}
.about-panel{left:590px;top:1005px;width:445px;height:310px;padding:10px 28px}
.about-body{position:absolute;left:140px;top:90px;width:280px}

/* packing */
.packing-bg{left:0;top:1380px;width:1200px;height:460px;background:linear-gradient(180deg,#fff 0%,var(--tint) 100%)}
.packing-photo{left:540px;top:1420px;width:660px;height:390px;background:linear-gradient(135deg,#d9dde2 0%,#b69a72 55%,#8d6d47 100%)}
.packing-panel{left:40px;top:1410px;width:480px;height:360px;padding:20px 28px}
.packing-body{position:absolute;left:40px;top:150px;width:320px}

/* contact */
.contact-photo{left:0;top:1870px;width:1200px;height:360px;background:linear-gradient(180deg,#e4e6ea 0%,#c8ccd3 100%)}
.contact-head{left:0;top:1920px;width:1200px}
.contact-head .section-title{font-size:48px}
.contact-note{left:240px;top:2055px;width:680px;display:flex;justify-content:space-between;font-size:11px;color:var(--ink)}
.contact-note span{width:320px;text-align:center}
.btn{height:52px;color:#fff;display:flex;align-items:center;justify-content:center;gap:10px;font-size:14px}
.btn-tel{left:240px;top:2080px;width:320px;background:var(--navy);flex-direction:column;gap:0}
.btn-tel small{font-size:9px;opacity:.8}
.btn-mail{left:600px;top:2080px;width:320px;background:var(--red)}

/* footer */
.site-footer{left:0;top:2230px;width:1200px;height:140px;background:#fff}
.footer-brand{left:260px;top:2262px;font-weight:700;font-size:20px;letter-spacing:4px;color:var(--navy)}
.footer-address{left:260px;top:2292px;font-size:10px;line-height:1.7;color:var(--ink)}
.footer-nav{left:690px;top:2262px;display:flex;gap:30px;font-size:10px;color:var(--ink)}
.copyright{left:0;top:2370px;width:1200px;height:18px;background:var(--navy-deep);color:#fff;font-size:8px;text-align:center;line-height:18px}
</style>
</head>
<body>

<header class="abs site-header">
  <div class="abs brand">LOGO</div>
  <nav class="abs global-nav"><span>ホーム</span><span>コンセプトについて</span><span>業務案内</span><span>会社概要</span></nav>
  <div class="abs header-cta"><a class="tel">TEL.03-4820-1175</a><a class="mail">お問い合わせ</a></div>
</header>

<section class="abs hero" role="img" aria-label="倉庫内に段ボールが積まれた棚の通路の写真"></section>
<div class="abs hero-copy">梱包が変わると<br>物流が変わる</div>

<div class="abs" style="right:0;top:642px;width:120px">
  <div class="stripe" style="background:var(--navy)"></div>
  <div class="stripe" style="background:#fff"></div>
  <div class="stripe" style="background:var(--red)"></div>
</div>

<div class="abs info-bg"></div>
<div class="abs info-head"><h2 class="section-title">Information</h2><p class="section-sub">お知らせ</p></div>
<ul class="abs news">
  <li><time>2019.01.01</time><span class="tag">お知らせ</span><span class="text">年末年始の営業についてのお知らせです。</span></li>
  <li><time>2019.01.01</time><span class="tag">お知らせ</span><span class="text">ホームページを公開いたしました。</span></li>
  <li><time>2019.01.01</time><span class="tag">お知らせ</span><span class="text">新しい梱包サービスを開始いたしました。</span></li>
  <li><time>2019.01.01</time><span class="tag">お知らせ</span><span class="text">夏季休業期間についてのお知らせです。</span></li>
</ul>

<div class="abs about-photo" role="img" aria-label="配送センターに並ぶトラックの荷台の写真"></div>
<section class="abs about-panel panel">
  <h2 class="heading">About</h2><p class="sub">コンセプトについて</p>
  <div class="about-body">
    <p>私たちは梱包の工夫を通じて、物流全体の品質と効率を高めることを目指しています。お客様の大切な荷物を安全に届けます。</p>
    <span class="more">VIEW MORE</span>
  </div>
</section>

<div class="abs packing-bg"></div>
<div class="abs packing-photo" role="img" aria-label="作業員が段ボール箱を梱包する様子の写真"></div>
<section class="abs packing-panel panel">
  <h2 class="heading">Packing</h2><p class="sub">業務案内</p>
  <div class="packing-body">
    <p>商品の特性に合わせた最適な梱包方法をご提案します。資材選びから作業まで一貫して対応し、コスト削減にも貢献いたします。</p>
    <span class="more">VIEW MORE</span>
  </div>
</section>

<div class="abs contact-photo" role="img" aria-label="物流センターの外観を淡く加工した写真"></div>
<div class="abs contact-head"><h2 class="section-title">Contact</h2><p class="section-sub">お問い合わせ</p></div>
<div class="abs contact-note"><span>お電話でのお問い合わせ</span><span>メールでのお問い合わせ</span></div>
<a class="abs btn btn-tel"><span>TEL.03-4820-1175</span><small>受付 9:00〜18:00</small></a>
<a class="abs btn btn-mail">
  <svg width="18" height="13" viewBox="0 0 18 13"><rect x="0.5" y="0.5" width="17" height="12" fill="none" stroke="#fff"/><path d="M1 1l8 6 8-6" fill="none" stroke="#fff"/></svg>
  <span>メールフォームはこちら</span>
</a>

<footer class="abs site-footer"></footer>
<div class="abs footer-brand">LOGO</div>
<p class="abs footer-address">〒000-0000 東京都港区芝浦1-2-3<br>TEL 03-4820-1175 / FAX 03-4820-1176</p>
<nav class="abs footer-nav"><span>ホーム</span><span>コンセプトについて</span><span>業務案内</span><span>会社概要</span></nav>
<div class="abs copyright">Copyright © LOGO All Rights Reserved.</div>

</body>
</html>
```